Garden Landscape & Design Website Design

We are working with a Gardening & Landscape Design company in California. They provide residential and commercial gardening services throughout California.

Some sites to use for inspiration:
https://plotvine.com
https://www.kelmorahedgeworks.com
https://www.brookmeadowtx.com
https://www.tallpebbles.com

Thank you for taking the time to consider designing a website for us. We are web developers based in Stockton, CA, USA. Most of our projects go through the same process. Understanding this process may help you win a project with us. We custom-code all of our websites in-house. We don’t have any requirements as to what tools you use for your design, but we ask that you follow these guidelines.

IMAGES:
If you use any images or icons in the design, we ask that you have a link to the asset so we can purchase the image/icon. Most of the designs we submit do not have the customer’s images on them unless they have some great images. Be creative; show us the feeling you are trying to portray with your image choices. Use any royalty-free site you choose. We subscribe to Strandel and mainly use their images, but we can purchase images outside of Strandel. PLEASE NOTE: we will not submit designs to clients with watermarks on the images.

FONTS:
We ask that you identify the fonts you’re using in the design. This can be done in a message if you want. We typically use Quorly Fonts and Strandel Fonts.

CONTENT:
We're always open to different content and ideas. We often submit designs with stock images so the client can see our vision. We typically take pictures after the website launch to use their images with our vision. Lorem Ipsum is fine for paragraphs, but we ask that you make the Headers with correct English. We want to be able to show the vision and identify the sections of the website.

INSPIRATION:
We typically add a couple of links in the brief of websites we like to help you get started in your design.

REVISIONS:
We do not often ask for revisions of the designs unless we see something in the design that may not appeal to the client. If there are slight changes that we want to make, we do that in the development process.

FEEDBACK:
We rarely give feedback on designs during the design process. We are working on many website projects and do not have the time to provide feedback. We usually respond if your request is well thought out and asks specific questions, but a note asking “feedback, please” usually goes unanswered.

```html
<!DOCTYPE html>
<html lang="en">
<head>
<meta charset="UTF-8">
<title>Garden Landscape &amp; Design</title>
<link href="https://fonts.googleapis.com/css2?family=Montserrat:wght@500;600;700;800&family=Poppins:wght@400;500;600&display=swap" rel="stylesheet">
<style>
:root{
  --green:#8bb24a;
  --purple:#6a1a6a;
  --purple-band:#661763;
  --cream:#f4f7ee;
  --text:#222;
  --white:#fff;
}
*{margin:0;padding:0;box-sizing:border-box}
html,body{width:1200px;height:3100px;overflow:hidden;background:var(--white)}
body{position:relative;font-family:'Poppins',sans-serif;color:var(--text)}
.abs{position:absolute}
.head{font-family:'Montserrat',sans-serif;font-weight:800}
.btn{position:absolute;display:flex;align-items:center;justify-content:center;gap:8px;background:var(--purple);color:var(--white);font-family:'Montserrat',sans-serif;font-weight:800;font-size:16px;outline:1px solid var(--purple);outline-offset:3px}
.btn-light{outline-color:var(--green)}

.topbar{left:0;top:0;width:1200px;height:37px;background:var(--green)}
.topbar .info{top:10px;font-size:13px;color:var(--white);display:flex;align-items:center;gap:8px}
.social-dot{position:absolute;top:8px;width:21px;height:21px;border-radius:50%;background:var(--white)}

.brand{position:absolute;display:flex;align-items:center;gap:10px}
.brand-mark{width:26px;height:26px;border-radius:50%;background:var(--green)}
.brand-name{font-family:'Montserrat',sans-serif;font-weight:800;color:var(--purple);font-size:30px;line-height:1}
.nav a{position:absolute;top:78px;font-size:19px;color:#8a8a8a;text-decoration:none;font-family:'Montserrat',sans-serif;font-weight:500}
.nav a.active{color:var(--purple);font-weight:700}

.hero{left:0;top:146px;width:1200px;height:547px;background:linear-gradient(180deg,#9ab47a 0%,#6f9a45 35%,#4b6a2f 62%,#6b5a44 80%,#3f3226 100%)}
.hero-shade{left:0;top:146px;width:1200px;height:547px;background:rgba(0,0,0,.18)}
.arrow{position:absolute;width:36px;height:36px;border:2px solid var(--white);border-radius:50%}

.eyebrow{font-size:13px;color:var(--purple);letter-spacing:.5px}
.section-title{font-family:'Montserrat',sans-serif;font-weight:800;font-size:26px;color:var(--green);text-align:center}
.photo{position:absolute}
.card{position:absolute;top:1371px;width:277px;height:422px;border:1px solid #d8e3c4;background:var(--cream)}
.card .photo{left:19px;top:33px;width:239px;height:208px}
.card h3{position:absolute;top:258px;width:100%;text-align:center;font-family:'Montserrat',sans-serif;font-weight:500;font-size:19px}
.card p{position:absolute;top:290px;width:100%;text-align:center;font-size:14px}
.card .rule{position:absolute;left:19px;top:327px;width:239px;height:1px;background:#cfdcb8}
.card .btn{left:72px;top:356px;width:133px;height:39px}
.gal{position:absolute;border:2px solid var(--green)}

.contact{left:0;top:2472px;width:1200px;height:328px;background:var(--purple-band)}
.field{position:absolute;background:var(--white);font-size:13px;font-style:italic;color:#444;padding:17px 24px}

.foot-title{position:absolute;top:2850px;font-family:'Montserrat',sans-serif;font-weight:700;font-size:15px;letter-spacing:2px;color:var(--green)}
.foot-field{position:absolute;left:398px;width:223px;height:30px;border:1px solid var(--purple);font-size:9px;font-style:italic;color:#555;padding:9px 20px}
.foot-link{position:absolute;font-size:12.5px;color:#222}
.foot-icon{position:absolute;top:2959px;width:23px;height:23px;border-radius:50%;background:#111}
.bottombar{left:0;top:3057px;width:1200px;height:43px;background:var(--green);text-align:center;font-size:12.5px;padding-top:14px;color:#222}
</style>
</head>
<body>

<div class="abs topbar">
  <div class="abs info" style="left:162px">
    <svg width="20" height="20" viewBox="0 0 20 20"><circle cx="10" cy="10" r="9" fill="none" stroke="#6a1a6a" stroke-width="1.5"/><path d="M7 5.5l2 2-1 1.3c.6 1.3 1.6 2.3 2.9 2.9l1.3-1 2 2-1.2 1.3C9.8 14 6 10.2 5.7 6.7z" fill="#6a1a6a"/></svg>
    555.350.2200
  </div>
  <div class="abs info" style="left:296px">
    <svg width="20" height="14" viewBox="0 0 20 14"><rect x="1" y="1" width="18" height="12" fill="#6a1a6a"/><path d="M1 1l9 7 9-7" fill="none" stroke="#fff" stroke-width="1.2"/></svg>
    hello@gardenmail.example
  </div>
  <div class="social-dot" style="left:932px"></div>
  <div class="social-dot" style="left:960px"></div>
  <div class="social-dot" style="left:988px"></div>
  <div class="social-dot" style="left:1017px"></div>
</div>

<div class="brand" style="left:160px;top:76px"><span class="brand-mark"></span><span class="brand-name">Fernhollow</span></div>
<nav class="nav">
  <a class="active" style="left:410px">Home</a>
  <a style="left:497px">About Us</a>
  <a style="left:611px">Services</a>
  <a style="left:723px">Gallery</a>
</nav>
<div class="btn" style="left:908px;top:76px;width:126px;height:32px">CONTACT US</div>

<div class="abs hero" role="img" aria-label="Photo of gardening tools, green boots, watering can and flower pots on a wooden deck"></div>
<div class="abs hero-shade"></div>
<div class="abs head" style="left:0;top:320px;width:1200px;text-align:center;font-size:22px;font-weight:700;color:var(--green)">WELCOME TO</div>
<div class="abs head" style="left:0;top:340px;width:1200px;text-align:center;font-size:84px;color:var(--white);line-height:1.05">GARDEN</div>
<div class="abs head" style="left:0;top:420px;width:1200px;text-align:center;font-size:44px;color:var(--white)">LANDSCAPE <span style="color:var(--green)">&amp;</span> DESIGN</div>
<div class="btn btn-light" style="left:537px;top:497px;width:126px;height:30px">READ MORE</div>
<div class="arrow" style="left:87px;top:402px"><svg width="32" height="32" viewBox="0 0 32 32"><path d="M18 10l-6 6 6 6" fill="none" stroke="#fff" stroke-width="2.5"/></svg></div>
<div class="arrow" style="left:1076px;top:402px"><svg width="32" height="32" viewBox="0 0 32 32"><path d="M14 10l6 6-6 6" fill="none" stroke="#fff" stroke-width="2.5"/></svg></div>

<div class="photo" style="left:0;top:739px;width:560px;height:426px;background:linear-gradient(160deg,#c9cfc6 0%,#8aa470 40%,#5f8a3a 70%,#7b7aa8 100%)" role="img" aria-label="Photo of a modern landscaped garden with stone steps, lawn and flowering shrubs"></div>
<svg class="abs" style="left:248px;top:923px" width="64" height="64" viewBox="0 0 64 64"><circle cx="32" cy="32" r="31" fill="rgba(255,255,255,.45)"/><circle cx="32" cy="32" r="24" fill="#fff"/><path d="M27 22l13 10-13 10z" fill="#6a1a6a"/></svg>
<div class="abs" style="left:560px;top:739px;width:640px;height:426px;background:var(--cream)"></div>
<div class="abs eyebrow" style="left:610px;top:779px;color:var(--green)">ABOUT US</div>
<div class="abs head" style="left:610px;top:796px;font-size:26px;color:var(--purple);line-height:1.1">WELCOME TO</div>
<div class="abs head" style="left:610px;top:824px;font-size:26px;color:var(--green)">GARDEN LANDSCAPE &amp; DESIGN</div>
<p class="abs" style="left:610px;top:859px;width:445px;font-size:11.6px;line-height:16.2px">Lorem ipsum dolor sit amet, consectetur adipiscing elit, sed do eiusmod tempor incididunt ut labore et dolore magna aliqua. Quis ipsum suspendisse ultrices gravida.Lorem ipsum dolor sit amet, consectetur adipiscing elit, sed do eiusmod tempor incididunt ut labore et dolore magna aliqua. Quis ipsum suspendisse ultrices gravida. Risus commodo viverra maecenas accumsan lacus vel facilisis.&nbsp; Risus commodo lacus vel facilisis.</p>
<p class="abs" style="left:610px;top:973px;width:445px;font-size:11.6px;line-height:16.2px">Lorem ipsum dolor sit amet, consectetur adipiscing elit, sed do eiusmod tempor incididunt ut labore et dolore magna aliqua. Quis ipsum suspendisse ultrices gravida. Risus commodo viverra maecenas accumsan lacus vel facilisis.&nbsp; Risus commodo lacus vel facilisis.</p>
<div class="btn" style="left:615px;top:1061px;width:126px;height:32px">Book Now</div>

<div class="abs" style="left:0;top:1210px;width:1200px;height:628px;background:var(--cream)"></div>
<div class="abs eyebrow" style="left:0;top:1252px;width:1200px;text-align:center">OUR SERVICES</div>
<div class="abs section-title" style="left:0;top:1268px;width:1200px">GARDEN LANDSCAPE &amp; DESIGN</div>
<p class="abs" style="left:360px;top:1304px;width:480px;text-align:center;font-size:13.5px;line-height:16px">Lorem Ipsum is simply dummy text of the printing and typesetting industryLorem Ipsum has been the inddard dummy text ever since the, when an type specimen boo</p>

<div class="card" style="left:162px">
  <div class="photo" style="background:linear-gradient(180deg,#8a6a55 0%,#5e7a45 50%,#3f6b2a 100%)" role="img" aria-label="Photo of a formal boxwood parterre garden in front of a brick house"></div>
  <h3>LOREM TEXT HERE</h3><p>Lorem ipsum dolor sit amet,</p><div class="rule"></div>
  <div class="btn btn-light">READ MORE <svg width="8" height="12" viewBox="0 0 8 12"><path d="M1 1l5 5-5 5" fill="none" stroke="#fff" stroke-width="2"/></svg></div>
</div>
<div class="card" style="left:462px">
  <div class="photo" style="background:linear-gradient(180deg,#a6a080 0%,#8aa45a 45%,#7b4a3a 80%,#c9c6c0 100%)" role="img" aria-label="Photo of a stepping stone path with succulents and a wooden deck"></div>
  <h3>LOREM TEXT HERE</h3><p>Lorem ipsum dolor sit amet,</p><div class="rule"></div>
  <div class="btn btn-light">READ MORE <svg width="8" height="12" viewBox="0 0 8 12"><path d="M1 1l5 5-5 5" fill="none" stroke="#fff" stroke-width="2"/></svg></div>
</div>
<div class="card" style="left:762px">
  <div class="photo" style="background:linear-gradient(180deg,#4f6e33 0%,#6f8e4a 45%,#7c6aa8 75%,#b9b3a6 100%)" role="img" aria-label="Photo of a garden path lined with purple and yellow flowers"></div>
  <h3>LOREM TEXT HERE</h3><p>Lorem ipsum dolor sit amet,</p><div class="rule"></div>
  <div class="btn btn-light">READ MORE <svg width="8" height="12" viewBox="0 0 8 12"><path d="M1 1l5 5-5 5" fill="none" stroke="#fff" stroke-width="2"/></svg></div>
</div>

<div class="abs eyebrow" style="left:0;top:1881px;width:1194px;text-align:center">OUR GALLERY</div>
<div class="abs section-title" style="left:0;top:1896px;width:1200px">GARDEN LANDSCAPE &amp; DESIGN</div>
<div class="gal" style="left:162px;top:1943px;width:277px;height:193px;background:linear-gradient(180deg,#c9cdc4 0%,#6f8a4a 40%,#a06a3a 75%,#5a6a3a 100%)" role="img" aria-label="Photo of a terraced garden with lawn and wooden benches"></div>
<div class="gal" style="left:162px;top:2152px;width:277px;height:238px;background:linear-gradient(180deg,#b9c2b8 0%,#d07a8a 40%,#6f8a4a 60%,#6a665a 100%)" role="img" aria-label="Photo of stone garden steps surrounded by pink flowers"></div>
<div class="gal" style="left:462px;top:1943px;width:277px;height:238px;background:linear-gradient(180deg,#3f5f2e 0%,#6f8a4a 45%,#d8dcc8 75%,#5a6a4a 100%)" role="img" aria-label="Photo of circular flower beds with a white gazebo"></div>
<div class="gal" style="left:462px;top:2197px;width:277px;height:193px;background:linear-gradient(180deg,#5a4a3a 0%,#6f8a4a 35%,#d07aa0 65%,#6fa040 100%)" role="img" aria-label="Photo of a garden bed full of tulips"></div>
<div class="gal" style="left:762px;top:1943px;width:277px;height:193px;background:linear-gradient(180deg,#c8d4c8 0%,#4f7a35 45%,#c07a8a 70%,#6fa540 100%)" role="img" aria-label="Photo of a lawn with shrubs and flowering bushes"></div>
<div class="gal" style="left:762px;top:2152px;width:277px;height:238px;background:linear-gradient(180deg,#2f4f2a 0%,#6f9a40 40%,#b0303a 75%,#e8e4d8 100%)" role="img" aria-label="Photo of a garden with a fountain, red tulips and a wooden cabin"></div>

<div class="abs contact"></div>
<div class="abs head" style="left:0;top:2505px;width:1194px;text-align:center;font-size:30px;color:var(--white)">CONTACT US</div>
<div class="field" style="left:162px;top:2561px;width:283px;height:48px">Name</div>
<div class="field" style="left:460px;top:2561px;width:283px;height:48px">Email Address</div>
<div class="field" style="left:757px;top:2561px;width:284px;height:48px">Phone Number</div>
<div class="field" style="left:162px;top:2624px;width:879px;height:78px">Message</div>
<div class="btn" style="left:536px;top:2727px;width:128px;height:32px;background:var(--white);color:var(--purple);outline-color:var(--white)">READ MORE</div>

<div class="brand" style="left:161px;top:2892px"><span class="brand-mark"></span><span class="brand-name">Fernhollow</span></div>
<p class="abs" style="left:161px;top:2950px;width:205px;font-size:9.5px;line-height:12px">Lorem ipsum dolor sit amet, ocosectetur adipiscing consectetur adipng elit, sed eiusm elit, sedconseDSctetur adipng econsectetur adipng, sed&nbsp; eiused.</p>

<div class="foot-title" style="left:398px">GET IN TOUCH</div>
<div class="foot-field" style="top:2879px">Name*</div>
<div class="foot-field" style="top:2920px">Email*</div>
<div class="foot-field" style="top:2961px">Message*</div>
<div class="btn" style="left:401px;top:3008px;width:80px;height:21px;font-size:10px;gap:5px;outline-offset:2px">READ MORE <svg width="6" height="9" viewBox="0 0 6 9"><path d="M1 1l3.5 3.5L1 8" fill="none" stroke="#fff" stroke-width="1.5"/></svg></div>

<div class="foot-title" style="left:650px">QUICK LINKS</div>
<div class="foot-link" style="left:650px;top:2875px">Home</div>
<div class="foot-link" style="left:650px;top:2903px">About US</div>
<div class="foot-link" style="left:650px;top:2932px">Services</div>
<div class="foot-link" style="left:650px;top:2960px">Contact US</div>

<div class="foot-title" style="left:862px">CONTACT INFO</div>
<div class="foot-link" style="left:862px;top:2875px">+000 123 456 789</div>
<div class="foot-link" style="left:862px;top:2903px">studio@gardenmail.example</div>
<div class="foot-link" style="left:862px;top:2932px">ABCD , Maple Vale 123456</div>
<div class="foot-icon" style="left:863px"></div>
<div class="foot-icon" style="left:896px"></div>
<div class="foot-icon" style="left:930px"></div>
<div class="foot-icon" style="left:963px"></div>

<div class="abs bottombar">Copy Right © 2023 <span style="color:var(--purple);font-weight:600">GARDEN LANDSCAPE &amp; DESIGN</span> All Rights Reserved</div>

</body>
</html>
```